Medical Marijuana Service in the Bay Area

This is for a business card design that is going to be making medical marijuana deliveries in the bay area. The name of the the business is "Silverpine Herbal Wellness". I would like to have a modern feel and showing us as a medical marijuana company but at the same time discrete about it. I'm trying to target more sophisticated clients.

Industry/Entity Type

Medical

Contact Information for Business Card

Would like people to know it is for medical marijuana but in a discrete way.

```html
<!DOCTYPE html>
<html lang="en">
<head>
<meta charset="UTF-8">
<title>Silverpine Herbal Wellness – Business Card</title>
<link rel="stylesheet" href="https://fonts.googleapis.com/css2?family=Cinzel:wght@700&family=Lato:wght@400;700&display=swap">
<style>
  :root {
    --backdrop: #232323;
    --card-black: #0b0b0b;
    --card-sheen: #1c1c1c;
    --brand-red: #e3303a;
    --mark-faint: #331d1b;
    --text-light: #f2f2f2;
  }
  * { margin: 0; padding: 0; box-sizing: border-box; }
  html, body {
    width: 1200px;
    height: 800px;
    overflow: hidden;
    background: var(--backdrop);
  }
  .canvas {
    position: relative;
    width: 1200px;
    height: 800px;
  }
  .card {
    position: absolute;
    width: 520px;
    height: 297px;
    border-radius: 18px;
    overflow: hidden;
    background: linear-gradient(135deg, var(--card-black) 0%, var(--card-sheen) 50%, var(--card-black) 100%);
    box-shadow: 0 10px 30px rgba(0,0,0,0.55);
  }
  .card--front { left: 100px; top: 120px; }
  .card--back { left: 580px; top: 383px; }

  .front-square {
    position: absolute;
    left: 175px;
    top: 64px;
    width: 170px;
    height: 170px;
    background: var(--mark-faint);
  }
  .front-name {
    position: absolute;
    left: 0;
    right: 0;
    top: 132px;
    text-align: center;
    font-family: "Cinzel", serif;
    font-weight: 700;
    font-size: 25px;
    letter-spacing: 0.5px;
    color: var(--brand-red);
  }

  .back-square {
    position: absolute;
    right: 44px;
    top: 40px;
    width: 118px;
    height: 118px;
    background: var(--brand-red);
  }
  .back-name {
    position: absolute;
    left: 40px;
    top: 176px;
    font-family: "Lato", sans-serif;
    font-weight: 700;
    font-size: 21px;
    color: var(--brand-red);
  }
  .contact-list {
    position: absolute;
    left: 40px;
    top: 214px;
    list-style: none;
    font-family: "Lato", sans-serif;
    font-size: 16px;
    color: var(--text-light);
  }
  .contact-item {
    display: flex;
    align-items: center;
    gap: 10px;
    margin-bottom: 8px;
  }
  .contact-icon { width: 14px; height: 14px; fill: var(--brand-red); flex: none; }
</style>
</head>
<body>
<main class="canvas">
  <section class="card card--front" aria-label="Card front">
    <div class="front-square"></div>
    <h1 class="front-name">Silverpine Herbal Wellness</h1>
  </section>

  <section class="card card--back" aria-label="Card back">
    <div class="back-square"></div>
    <h2 class="back-name">Silverpine Herbal Wellness</h2>
    <ul class="contact-list">
      <li class="contact-item">
        <svg class="contact-icon" viewBox="0 0 16 16" aria-hidden="true">
          <path d="M3 1h3l1.5 4-2 1.3a9 9 0 0 0 4.2 4.2L11 8.5l4 1.5v3a2 2 0 0 1-2 2A12 12 0 0 1 1 3a2 2 0 0 1 2-2z"/>
        </svg>
        <span>415-555-0142</span>
      </li>
      <li class="contact-item">
        <svg class="contact-icon" viewBox="0 0 16 16" aria-hidden="true">
          <path d="M1 3h14v10H1z M1.8 3.6 8 8.6l6.2-5" fill="none" stroke="#e3303a" stroke-width="0"/>
          <path d="M1 3h14v1.2L8 9 1 4.2z"/>
          <path d="M1 5.6 8 10.4l7-4.8V13H1z"/>
        </svg>
        <span>hello@silverpineherbal.com</span>
      </li>
    </ul>
  </section>
</main>
</body>
</html>
```